Commercial Real Estate Property Sign

Design a 4' x 4' sign that pops. Refer to examples.

Must include the following information:
A space to list (For Sale, For Lease, Build-to-Suite or Available)
Brightvale,LLC
Commercial Real Estate
company website
My Name (Marcus Pellew)
My Phone #

Industry/Entity Type

Real Estate

```html
<!DOCTYPE html>
<html lang="en">
<head>
<meta charset="utf-8">
<title>Brightvale, LLC – Commercial Real Estate Sign</title>
<link rel="stylesheet" href="https://fonts.googleapis.com/css2?family=Barlow:wght@400;600;700&display=swap">
<style>
  :root {
    --sign-orange: #e8660a;
    --sign-charcoal: #3b3b3b;
    --sign-ink: #1c1c1c;
    --sign-white: #ffffff;
  }
  * { margin: 0; padding: 0; box-sizing: border-box; }
  html, body {
    width: 1200px;
    height: 1200px;
    overflow: hidden;
  }
  body {
    background: var(--sign-orange);
    font-family: "Barlow", Arial, sans-serif;
    position: relative;
  }
  .sign {
    position: relative;
    width: 1200px;
    height: 1200px;
    background: var(--sign-orange);
  }
  .brand-block {
    position: absolute;
    left: 422px;
    top: 0;
    width: 356px;
    height: 499px;
    background: var(--sign-charcoal);
  }
  .brand-name {
    position: absolute;
    left: 34px;
    top: 222px;
    color: var(--sign-white);
    font-weight: 400;
    font-size: 60px;
    line-height: 90px;
    letter-spacing: 1px;
  }
  .brand-tagline {
    position: absolute;
    top: 508px;
    width: 100%;
    text-align: center;
    font-weight: 700;
    font-size: 28px;
    color: var(--sign-ink);
  }
  .agent-name {
    position: absolute;
    top: 594px;
    width: 100%;
    text-align: center;
    font-weight: 400;
    font-size: 82px;
    line-height: 100px;
    color: var(--sign-ink);
    letter-spacing: 1px;
  }
  .agent-phone {
    position: absolute;
    top: 684px;
    width: 100%;
    text-align: center;
    font-weight: 700;
    font-size: 86px;
    line-height: 100px;
    color: var(--sign-ink);
    letter-spacing: 3px;
  }
  .listing-band {
    position: absolute;
    left: 0;
    top: 830px;
    width: 1200px;
    height: 242px;
    background: var(--sign-charcoal);
    color: var(--sign-white);
    font-weight: 700;
    font-size: 76px;
    text-align: center;
  }
  .listing-line {
    position: absolute;
    width: 100%;
    line-height: 90px;
  }
  .listing-line.primary { top: 25px; }
  .listing-line.secondary { top: 137px; }
  .initial { color: var(--sign-orange); }
  .divider {
    display: inline-block;
    width: 3px;
    height: 58px;
    background: var(--sign-white);
    margin: 0 22px;
    vertical-align: -6px;
  }
  .website {
    position: absolute;
    top: 1106px;
    width: 100%;
    text-align: center;
    font-weight: 700;
    font-size: 44px;
    line-height: 54px;
    color: var(--sign-ink);
    letter-spacing: 1px;
  }
  .web-icon {
    width: 30px;
    height: 30px;
    vertical-align: -3px;
    margin-right: 10px;
  }
</style>
</head>
<body>
  <main class="sign">
    <section class="brand-block">
      <div class="brand-name">Brightvale,<br>LLC</div>
    </section>
    <p class="brand-tagline">Commercial Real Estate</p>

    <p class="agent-name">Marcus Pellew</p>
    <p class="agent-phone">555.014.2870</p>

    <section class="listing-band">
      <p class="listing-line primary"><span class="initial">F</span>or Sale<span class="divider"></span><span class="initial">F</span>or Lease</p>
      <p class="listing-line secondary"><span class="initial">B</span>uild-to-Suite or Available</p>
    </section>

    <p class="website">
      <svg class="web-icon" viewBox="0 0 24 24" fill="none" stroke="#1c1c1c" stroke-width="2" aria-hidden="true">
        <circle cx="12" cy="12" r="10"/>
        <ellipse cx="12" cy="12" rx="4.5" ry="10"/>
        <line x1="2" y1="12" x2="22" y2="12"/>
      </svg>www.mybrightvale.com
    </p>
  </main>
</body>
</html>
```